Greenloop Advisors, LLC

I am looking for a simple, clear layout with my logo prominent and embossed, on the best quality card stock available. I would like the business name and phone number included on the card as well......I dont want my name anywhere on the card and I would like my logo embossed on the card......something simple with a white back......open to designs as long as they go along with recycling symbols and green type stuff.....The address, website, cell number, fax number, and email are listed below

4637 Pellmont Carrow Road
Fernwick, MD 20917

c. 240.555.3184 f. 240.555.6052
e. sales@greenloopadvisors.example
w. www.greenloopadvisors.example

Industry/Entity Type

Recycling

```html
<!DOCTYPE html>
<html lang="en">
<head>
<meta charset="utf-8">
<title>Greenloop Advisors, LLC — Business Card</title>
<link rel="stylesheet" href="https://fonts.googleapis.com/css2?family=Barlow:wght@400;700&display=swap">
<style>
  :root {
    --backdrop: #e7e4df;
    --card: #f7f6f2;
    --ink: #2e2b28;
    --ink-soft: #3b3835;
    --leaf: #1f7a45;
    --shadow: rgba(0, 0, 0, 0.18);
  }
  html, body {
    margin: 0;
    width: 1200px;
    height: 800px;
    overflow: hidden;
    background: var(--backdrop);
  }
  .card {
    position: absolute;
    left: 145px;
    top: 140px;
    width: 910px;
    height: 520px;
    background: var(--card);
    box-shadow: 0 10px 30px var(--shadow);
    font-family: "Barlow", sans-serif;
    color: var(--ink);
  }
  .brand {
    position: absolute;
    left: 90px;
    top: 110px;
    display: flex;
    align-items: center;
    gap: 26px;
  }
  .brand-mark {
    width: 62px;
    height: 62px;
    background: var(--leaf);
  }
  .brand-name {
    margin: 0;
    font-size: 52px;
    font-weight: 700;
    letter-spacing: 1px;
    text-transform: uppercase;
    color: var(--ink);
    line-height: 1;
    white-space: nowrap;
  }
  .contact {
    position: absolute;
    left: 290px;
    top: 262px;
    font-size: 24px;
    line-height: 33px;
    color: var(--ink-soft);
  }
  .contact p { margin: 0; }
  .contact .address { margin-top: 10px; }
  .label { text-transform: uppercase; }
  .gap { display: inline-block; width: 22px; }
  .rule {
    width: 320px;
    height: 2px;
    background: var(--leaf);
    margin: 6px 0 16px;
  }
</style>
</head>
<body>
  <article class="card">
    <header class="brand">
      <div class="brand-mark" aria-hidden="true"></div>
      <h1 class="brand-name">Greenloop Advisors, LLC</h1>
    </header>
    <section class="contact">
      <p><span class="label">Phone</span> 240.555.3184<span class="gap"></span><span class="label">Fax</span> 240.555.6052</p>
      <p><span class="label">Email</span> sales@greenloopadvisors.example</p>
      <p class="address">4637 Pellmont Carrow Road<br>Fernwick, MD 20917</p>
      <div class="rule"></div>
      <p class="website">www.greenloopadvisors.example</p>
    </section>
  </article>
</body>
</html>
```